Broschüren-Design für Bettenmanufaktur
Super Design, super schnelle Reaktion, super netter Kontakt!
Zielgruppe
Wir sind eine Bettenmanufaktur die Futonbetten und Himmelbetten aus Metall herstellt, geziert mit Leder- oder Holzelementen an den Bettseiten und Rückenlehnen. Das besondere ist, dass es Systembetten sind. Man kann später aus seinen Futonbett noch ein Himmelbett machen, oder die Leder- und Holzelemente einfach tauschen. Unsere Zielgruppe sind Paare die auf Design und Still stehen, sowie auf Paare die Lust auf Mehr als nur ein Bett haben.
Aufgabenstellung
Bitte an unsere neue Homepage vom Design/Still anpassen: www.trovalin-design.de
Die Broschüre soll als Zulage bei anderen Bestellungen beiliegen und auf Messen verteilt werden.

```html
<!DOCTYPE html>
<html lang="de">
<head>
<meta charset="utf-8">
<title>lichtfaltwerk – Broschüre und Flyer</title>
<link rel="stylesheet" href="https://fonts.googleapis.com/css2?family=Montserrat:ital,wght@0,400;0,500;0,700;1,500&family=Saira+Semi+Condensed:wght@700&display=swap">
<style>
  :root {
    --red: #bf3a2a;
    --black: #262626;
    --ink: #1c1c1c;
    --white: #ffffff;
    --canvas: #f4f3f1;
    --photo-warm-a: #4a3a2c;
    --photo-warm-b: #2b221b;
    --photo-red-a: #7a2a1e;
    --photo-red-b: #3a2a22;
    --photo-room-a: #5a5a5e;
    --photo-room-b: #232326;
    --photo-studio-a: #eeeeee;
    --photo-studio-b: #bdbdbd;
  }
  * { box-sizing: border-box; margin: 0; padding: 0; }
  html, body { width: 1200px; height: 800px; overflow: hidden; }
  body {
    background: var(--canvas);
    font-family: "Montserrat", sans-serif;
    color: var(--white);
    position: relative;
  }

  /* ---------- Trifold brochure ---------- */
  .brochure {
    position: absolute; left: 40px; top: 120px;
    width: 780px; height: 560px;
    display: flex;
    box-shadow: 0 10px 30px rgba(0,0,0,.18);
  }
  .panel { position: relative; width: 260px; height: 100%; overflow: hidden; }
  .photo { position: absolute; }

  .panel--about .photo--curtains {
    inset: 0 0 260px 0;
    background: linear-gradient(160deg, var(--photo-warm-a), var(--photo-warm-b));
  }
  .panel--about .photo--room {
    left: 0; right: 0; bottom: 0; height: 260px;
    background: linear-gradient(180deg, var(--photo-room-a), var(--photo-room-b));
  }
  .about-text { position: absolute; left: 22px; right: 18px; top: 46px; }
  .about-text h2 { font-size: 15px; font-weight: 700; letter-spacing: .04em; margin-bottom: 14px; }
  .about-text p { font-size: 9.6px; line-height: 1.6; letter-spacing: .02em; }

  .panel--intro .photo--bedroom {
    inset: 0 0 260px 0;
    background: linear-gradient(150deg, var(--photo-red-b) 10%, var(--photo-red-a) 60%, var(--photo-red-b));
  }
  .brand {
    position: absolute; top: 34px; left: 0; right: 0;
    font-size: 22px; font-weight: 500; letter-spacing: .01em;
    display: flex; align-items: center; justify-content: center; gap: 6px;
  }
  .brand-dot { width: 8px; height: 8px; border-radius: 50%; background: var(--white); }
  .quote-mark { font-family: "Montserrat", sans-serif; font-weight: 700; line-height: 1; }
  .panel--intro .quote-mark { position: absolute; top: 70px; left: 70px; font-size: 96px; }
  .tagline { position: absolute; left: 50px; top: 160px; font-size: 19px; line-height: 1.5; letter-spacing: .06em; }
  .tagline span { display: block; }
  .tagline span:nth-child(2) { padding-left: 12px; }
  .tagline span:nth-child(3) { padding-left: 24px; }

  .gallery {
    position: absolute; left: 0; right: 0; bottom: 0; height: 260px;
    background: var(--black);
    display: grid; grid-template-columns: 1fr 1fr; gap: 10px; padding: 14px;
  }
  .gallery .tile { background: linear-gradient(160deg, var(--photo-studio-a), var(--photo-studio-b)); }
  .gallery .tile--dark { background: linear-gradient(180deg, #3a3a3a, #8a2a22); }

  .panel--range { background: var(--red); }
  .range { position: absolute; left: 20px; right: 16px; top: 30px; }
  .range h2 { font-size: 12.5px; font-weight: 700; letter-spacing: .05em; margin-bottom: 16px; }
  .range h3 { font-size: 10px; font-weight: 700; letter-spacing: .05em; margin-bottom: 4px; }
  .range p { font-size: 9.4px; line-height: 1.5; letter-spacing: .02em; margin-bottom: 14px; }
  .range .lead { font-style: italic; font-weight: 500; font-size: 10px; }
  .panel--range .photo--product {
    right: 0; top: 330px; width: 150px; height: 150px;
    background: linear-gradient(160deg, #e8e8e8, #9a9a9a);
  }
  .range-footnote {
    position: absolute; left: 20px; top: 492px; width: 110px;
    font-size: 9.4px; line-height: 1.5; letter-spacing: .02em;
  }

  /* ---------- Rack card ---------- */
  .card {
    position: absolute; left: 890px; top: 100px;
    width: 270px; height: 600px;
    background: var(--red);
    box-shadow: 0 10px 30px rgba(0,0,0,.18);
    overflow: hidden;
    display: flex; flex-direction: column;
  }
  .card-top { position: relative; height: 236px; flex: none; }
  .card .photo--strip {
    left: 0; top: 0; width: 34px; height: 100%;
    background: linear-gradient(180deg, #5a4a52, #7a2a2a 50%, #4a4a4a);
  }
  .feather {
    position: absolute; width: 56px; height: 104px;
    background: linear-gradient(160deg, rgba(255,255,255,.35), rgba(255,255,255,.08));
    border-radius: 50% 50% 50% 50% / 60% 60% 40% 40%;
  }
  .feather--top { left: 46px; top: 16px; transform: rotate(-20deg); }
  .feather--bottom { right: 18px; top: 16px; transform: rotate(-10deg); }
  .card-top .quote-mark { position: absolute; right: 28px; top: 20px; font-size: 46px; }
  .card-tagline {
    position: absolute; right: 26px; top: 80px; text-align: right;
    font-size: 17px; line-height: 1.65; letter-spacing: .05em;
  }
  .card-band {
    flex: none;
    background: var(--ink);
    font-family: "Saira Semi Condensed", "Arial Narrow", sans-serif; font-weight: 700;
    padding: 18px 12px 18px 16px;
  }
  .card-band p { white-space: nowrap; }
  .card-band .promise { color: var(--red); font-size: 25px; line-height: 1.12; }
  .card-band .product { color: var(--white); font-size: 24px; line-height: 1.12; margin-top: 14px; text-align: center; }
  .card-bottom { position: relative; flex: 1; }
  .card .photo--strip-low {
    left: 0; top: 0; width: 34px; height: 70px;
    background: linear-gradient(180deg, #333, #1c1c1c);
  }
  .card-bottom .quote-mark { position: absolute; left: 70px; top: 10px; font-size: 36px; }
  .card-values {
    position: absolute; left: 72px; top: 46px;
    font-style: italic; font-weight: 500; font-size: 14px; line-height: 1.55; letter-spacing: .04em;
  }
  .card-rule { position: absolute; left: 0; right: 0; bottom: 18px; height: 1px; background: rgba(255,255,255,.8); }
</style>
</head>
<body>

<section class="brochure">
  <article class="panel panel--about">
    <div class="photo photo--curtains" role="img" aria-label="Foto: Himmelbett mit Vorhängen in warmem Licht"></div>
    <div class="photo photo--room" role="img" aria-label="Foto: dunkles Schlafzimmer mit Metall-Futonbett vor hohen Fenstern"></div>
    <div class="about-text">
      <h2>ÜBER UNS</h2>
      <p>Unser Team begleitet Sie bei der Planung Ihres individuellen System-Metallbetts. Wir setzen Ihre Wünsche und Fantasien um und bringen Ihre Träume in die Realität. Alle Komponenten werden entweder in unserer firmeneigenen Manufaktur oder von regional ansässigen Handwerks-betrieben gefertigt. Mit Fachkompetenz und Sorgfalt garantieren wir dafür, dass sich alle Einzelteile zu einem perfekten Ensemble zusammenfügen.</p>
    </div>
  </article>

  <article class="panel panel--intro">
    <div class="photo photo--bedroom" role="img" aria-label="Foto: Himmelbett mit roter Bettwäsche und Stoffbahnen"></div>
    <div class="brand">lichtfaltwerk<span class="brand-dot"></span></div>
    <div class="quote-mark">“</div>
    <p class="tagline"><span>Futonbett.</span><span>Himmelbett.</span><span>Lustbett.</span></p>
    <div class="gallery">
      <div class="tile tile--dark" role="img" aria-label="Foto: Paar auf einem Himmelbett mit roter Bettwäsche"></div>
      <div class="tile" role="img" aria-label="Foto: leeres Metall-Himmelbett im Studio"></div>
      <div class="tile" role="img" aria-label="Foto: Metall-Himmelbett mit Bildtafel im Studio"></div>
      <div class="tile" role="img" aria-label="Foto: Futonbett mit roter Bettwäsche im Studio"></div>
    </div>
  </article>

  <article class="panel panel--range">
    <div class="range">
      <h2>TROVALIN - METALLBETTEN</h2>
      <h3>I SYSTEM-HIMMELBETT ULTIMATE</h3>
      <p>Klares Design und individuelle Gestaltungsfreiheit für hohe Ansprüche.</p>
      <h3>II SYSTEM-HIMMELBETT ADVANCED</h3>
      <p>Perfekte nächtliche Regeneration und niveauvolle gemeinsame Stunden.</p>
      <h3>III METALL-SYSTEMBETT CLASSIC</h3>
      <p>Puristischer Ruhepool und inspirierende Quelle für Ihre Fantasien.</p>
      <p class="lead">Erleben Sie einzigartigen Komfort und erkunden Sie neue erotische Horizonte.</p>
    </div>
    <div class="photo photo--product" role="img" aria-label="Foto: Metall-Himmelbett mit Stange im Studio"></div>
    <p class="range-footnote">Mit unserem System passen Sie Ihr Bett jederzeit an Ihre Wünsche an.</p>
  </article>
</section>

<aside class="card">
  <div class="card-top">
    <div class="photo photo--strip" role="img" aria-label="Foto: Ausschnitt Stoffe und Bettdetails"></div>
    <div class="feather feather--top" role="img" aria-label="Illustration: Feder"></div>
    <div class="quote-mark">“</div>
    <p class="card-tagline">Futonbett.<br>Himmelbett.<br>Lustbett.</p>
  </div>
  <div class="card-band">
    <p class="promise">IHRE WÜNSCHE.<br>IHRE NÄCHTE.<br>IHRE TRÄUME.</p>
    <p class="product">UNSER METALL-<br>SYSTEMBETT.</p>
  </div>
  <div class="card-bottom">
    <div class="photo photo--strip-low" role="img" aria-label="Foto: Ausschnitt gesteppte Matratze"></div>
    <div class="quote-mark">“</div>
    <p class="card-values">Sinnlich.<br>Exklusiv.<br>Fesselnd.</p>
    <div class="feather feather--bottom" role="img" aria-label="Illustration: Feder"></div>
    <div class="card-rule"></div>
  </div>
</aside>

</body>
</html>
```